Lorna Pettibone Nook Charmer

a larger business card may standard size 4” x 9” describing what I do. I don’t know if this would be considered a flyer. I rearrange, redesign and stage houses for the owner or to sell.

```html
<!DOCTYPE html>
<html lang="en">
<head>
<meta charset="utf-8">
<title>Lorna Pettibone – Nook Charmer cards</title>
<link rel="stylesheet" href="https://fonts.googleapis.com/css2?family=Raleway:ital,wght@0,300;0,400;0,500;0,700;0,800;1,600&display=swap">
<style>
  :root {
    --stage: #151515;
    --card: #ffffff;
    --brick: #8e2a1c;
    --terracotta: #e8874b;
    --band-grey: #d9d8d8;
    --sky: #a9bccb;
    --adobe: #d9773f;
  }
  html, body {
    margin: 0;
    padding: 0;
    width: 1200px;
    height: 741px;
    overflow: hidden;
    background: var(--stage);
    font-family: "Raleway", sans-serif;
  }
  .canvas {
    position: relative;
    width: 1200px;
    height: 741px;
  }
  .rack-card {
    position: absolute;
    left: 165px;
    top: 77px;
    width: 262px;
    height: 584px;
  }
  .business-card {
    position: absolute;
    left: 458px;
    width: 588px;
    height: 260px;
  }
  .business-card--top { top: 97px; }
  .business-card--bottom { top: 390px; }
  svg text { font-family: "Raleway", sans-serif; }
  .defs-only { position: absolute; width: 0; height: 0; }
</style>
</head>
<body>
<main class="canvas">

  <!-- tall rack card -->
  <svg class="rack-card" viewBox="0 0 318 709" aria-label="Rack card: home rearranged, redesigned, staged to sell">
    <defs>
      <clipPath id="rack-shape"><rect width="318" height="709" rx="28"/></clipPath>
      <linearGradient id="home-photo-tone" x1="0" y1="0" x2="0" y2="1">
        <stop offset="0" stop-color="var(--sky)"/>
        <stop offset="0.22" stop-color="#b7aea3"/>
        <stop offset="0.32" stop-color="#8f6f5c"/>
        <stop offset="0.45" stop-color="var(--adobe)"/>
        <stop offset="0.8" stop-color="#b35f34"/>
        <stop offset="1" stop-color="#6f5a3e"/>
      </linearGradient>
    </defs>
    <g clip-path="url(#rack-shape)">
      <rect class="rack-card__base" width="318" height="709" fill="var(--card)"/>
      <polygon class="rack-card__photo" role="img" aria-label="Photo of a terracotta adobe home with palms in front of desert mountains"
               points="0,0 318,0 318,266 160,372 0,266" fill="url(#home-photo-tone)"/>
      <polyline class="rack-card__chevron-line" points="0,296 160,386 318,296" fill="none" stroke="var(--brick)" stroke-width="4"/>
      <polygon class="rack-card__accent" points="183,423 318,317 318,500" fill="var(--terracotta)"/>
      <polygon class="rack-card__band" points="0,319 318,500 318,622 0,427" fill="var(--brick)"/>
      <g class="rack-card__tagline" fill="#ffffff" font-size="15.5">
        <text transform="translate(86,392) rotate(32)" x="0" y="12" textLength="226" lengthAdjust="spacing">WITH LITTLE OR NO COST,</text>
        <text transform="translate(98,434) rotate(32)" x="0" y="12" font-weight="800" textLength="162" lengthAdjust="spacing">LORNA BREATHES</text>
        <text transform="translate(10,406) rotate(32)" x="0" y="12" textLength="336" lengthAdjust="spacing">NEW LIFE &amp; ENERGY INTO YOUR HOME.</text>
      </g>
      <text class="rack-card__heading" x="23" y="572" font-size="22" font-weight="700" fill="var(--brick)">HOME:</text>
      <rect class="rack-card__rule" x="27" y="587" width="3" height="77" fill="var(--brick)"/>
      <g class="rack-card__services" font-size="22.5" fill="var(--brick)" font-weight="400">
        <text x="43" y="607" textLength="187" lengthAdjust="spacing"><tspan font-weight="700">RE</tspan>ARRANGED</text>
        <text x="43" y="636" textLength="175" lengthAdjust="spacing"><tspan font-weight="700">RE</tspan>DESIGNED</text>
        <text x="43" y="665" textLength="230" lengthAdjust="spacing">STAGED TO <tspan font-weight="800">SELL</tspan></text>
      </g>
    </g>
  </svg>

  <!-- shared business card artwork -->
  <svg class="defs-only" aria-hidden="true">
    <defs>
      <clipPath id="front-shape"><rect width="714" height="316" rx="40"/></clipPath>
      <linearGradient id="portrait-tone" x1="0" y1="0" x2="1" y2="1">
        <stop offset="0" stop-color="#cfc6c0"/>
        <stop offset="0.5" stop-color="#c9958a"/>
        <stop offset="1" stop-color="#5a3a2c"/>
      </linearGradient>
      <symbol id="front-card" viewBox="0 0 714 316">
        <g clip-path="url(#front-shape)">
          <rect class="front__base" width="714" height="316" fill="var(--card)"/>
          <rect class="front__band" x="0" y="33" width="430" height="107" fill="var(--band-grey)"/>
          <rect class="front__band-edge" x="0" y="33" width="12" height="107" fill="var(--brick)"/>
          <text class="front__name" x="186" y="64" text-anchor="middle" font-size="22" fill="var(--brick)"><tspan font-weight="700">LORNA</tspan> PETTIBONE</text>
          <text class="front__title" x="186" y="80" text-anchor="middle" font-size="13" fill="var(--brick)" font-weight="300">Nook Charmer</text>
          <text class="front__award" x="186" y="104" text-anchor="middle" font-size="15.5" letter-spacing="1.3" fill="var(--brick)">As a <tspan font-weight="800">BRIGHT HOMES &amp; YARDS</tspan></text>
          <text class="front__award" x="186" y="124" text-anchor="middle" font-size="13.5" letter-spacing="1.4" fill="var(--brick)">NATIONAL AWARD WINNER!</text>
          <circle class="front__portrait-ring" cx="421" cy="87" r="54" fill="#ffffff" stroke="var(--terracotta)" stroke-width="4"/>
          <circle class="front__portrait" role="img" aria-label="Portrait photo of Lorna Pettibone" cx="421" cy="87" r="50" fill="url(#portrait-tone)"/>
          <text class="front__lead" x="48" y="176" font-size="15.5" fill="var(--brick)">Thrilled Customers Say...</text>
          <text class="front__quote" x="48" y="194" font-size="14.5" font-style="italic" font-weight="600" letter-spacing="0.4" fill="var(--brick)">“ This is just how I dreamed my home would look!”</text>
          <g class="front__contact" font-size="14" fill="var(--brick)">
            <circle cx="57" cy="229" r="7" fill="var(--terracotta)"/>
            <path d="M54 225.5 q0 5 5 7 l1.3-1.5 -1.6-1.2 -0.9 0.8 q-1.6-0.8-2.2-2.4 l0.8-0.9 -1.1-1.7 z" fill="#ffffff"/>
            <text x="71" y="234">503-555-0142</text>
            <circle cx="57" cy="249" r="7" fill="var(--terracotta)"/>
            <rect x="53" y="246" width="8" height="6" fill="none" stroke="#ffffff" stroke-width="1.2"/>
            <path d="M53 246 l4 3 4-3" fill="none" stroke="#ffffff" stroke-width="1.1"/>
            <text x="71" y="254">lornapettibone@mailnest.net</text>
            <circle cx="57" cy="268" r="7" fill="var(--terracotta)"/>
            <path d="M57 272.5 l-3-4.5 a3.3 3.3 0 1 1 6 0 z" fill="#ffffff"/>
            <circle cx="57" cy="266" r="1.2" fill="var(--terracotta)"/>
            <text x="71" y="273" xml:space="preserve">2461 S. Alder Drive   Yuma, AZ 85365</text>
          </g>
        </g>
      </symbol>
    </defs>
  </svg>

  <svg class="business-card business-card--top" viewBox="0 0 714 316" aria-label="Business card for Lorna Pettibone">
    <use href="#front-card"/>
  </svg>
  <svg class="business-card business-card--bottom" viewBox="0 0 714 316" aria-label="Business card for Lorna Pettibone">
    <use href="#front-card"/>
  </svg>

</main>
</body>
</html>
```